Clearpath Ledgers New Website

Please review the attached Design Brief with additional details. Thank you!

The goal is to create a website that effectively communicates the benefits of ClearPath Ledgers to eye care professionals. The website should streamline the process of understanding and utilizing ClearPath Ledgers' services, emphasizing improved patient outcomes, increased referrals, and enhanced patient engagement.

Target Market(s)

Eyecare Professionals

Number of Pages Required

4 page

```html
<!DOCTYPE html>
<html lang="en">
<head>
<meta charset="utf-8">
<title>ClearPath Ledgers</title>
<link href="https://fonts.googleapis.com/css2?family=Kumbh+Sans:wght@400;500;600;700&display=swap" rel="stylesheet">
<style>
:root{
  --topbar:#1a73ec;
  --brand:#1f3bff;
  --hero:#3f5cf6;
  --navy:#1a2bb5;
  --footer:#13269f;
  --ink:#1d1d1f;
  --body:#4a4a4a;
  --muted:#8a8a8a;
  --soft:#f3f3f3;
  --line:#8e9cff;
  --white:#fff;
}
*{box-sizing:border-box;margin:0;padding:0}
html,body{width:1200px;height:4774px;overflow:hidden}
body{font-family:"Kumbh Sans",sans-serif;color:var(--ink);background:var(--white);position:relative}
.abs{position:absolute}
section,header,footer{position:absolute;left:0;width:1200px}

/* top bar */
.topbar{top:0;height:52px;background:var(--topbar);color:var(--white);font-size:11px}
.topbar .item{position:absolute;top:16px;display:flex;align-items:center;gap:10px}
.dot-icon{width:20px;height:20px;border-radius:50%;background:var(--white);display:inline-flex;align-items:center;justify-content:center}
.dot-icon i{width:8px;height:8px;border-radius:50%;background:var(--topbar)}
.follow{right:135px}
.social-dot{width:20px;height:20px;border-radius:50%;background:var(--white);display:inline-block}

/* header */
.site-header{top:52px;height:75px;background:var(--white)}
.logo-box{position:absolute;left:135px;top:0;width:205px;height:96px;background:var(--white);border-radius:0 0 10px 10px;box-shadow:0 4px 14px rgba(0,0,0,.12);display:flex;align-items:center;justify-content:center;gap:8px;z-index:3}
.logo-square{width:16px;height:16px;background:var(--brand)}
.logo-name{font-size:19px;font-weight:600;color:var(--navy);line-height:1}
.nav{position:absolute;top:36px;font-size:11px;color:var(--ink)}
.nav.active{color:var(--brand);font-weight:600}
.btn{position:absolute;display:flex;align-items:center;justify-content:center;font-size:11px;border-right:3px solid rgba(255,255,255,.7)}
.btn::after{content:"";position:absolute;right:-8px;top:0;bottom:0;width:2px;background:inherit}
.btn-blue{background:var(--brand);color:var(--white)}
.btn-navy{background:var(--navy);color:var(--white)}
.btn-white{background:var(--white);color:var(--ink);border-right-color:#ccd}

/* hero */
.hero{top:127px;height:674px}
.hero-photo{position:absolute;left:0;top:0;width:640px;height:674px;background:linear-gradient(135deg,#e9e7e4,#cfc8c0 55%,#b9b0a6)}
.hero-panel{position:absolute;left:640px;top:0;width:560px;height:674px;background:linear-gradient(160deg,#4a67fb,#3350f0)}
.hero h1{position:absolute;right:137px;top:165px;text-align:right;color:var(--white);font-weight:500;font-size:50px;line-height:57px}
.hero p{position:absolute;right:137px;top:348px;width:290px;text-align:right;color:var(--white);font-size:13px;line-height:27px}
.scroll-line{position:absolute;left:1165px;width:2px;background:var(--white)}
.mouse{position:absolute;left:1154px;top:326px;width:22px;height:36px;border-radius:11px;background:var(--white)}
.mouse::after{content:"";position:absolute;left:10px;top:6px;width:2px;height:8px;background:var(--hero)}

/* features */
.features{top:801px;left:135px;width:928px;height:151px;background:var(--white);box-shadow:0 6px 20px rgba(0,0,0,.08)}
.feature{position:absolute;top:40px;width:250px}
.feature h3{font-size:17px;font-weight:500}
.feature h3 span{margin-right:10px;color:var(--ink)}
.feature p{margin:10px 0 0 44px;font-size:10px;line-height:19px;color:var(--body)}

/* about */
.about{top:1000px;height:670px}
.corner{position:absolute;background:var(--navy)}
.about-photo{position:absolute;left:150px;top:65px;width:490px;height:475px;background:linear-gradient(135deg,#e4e1dc,#c9c1b7 60%,#a59a8e)}
.about h2{position:absolute;left:720px;top:110px;font-size:40px;font-weight:500}
.about p{position:absolute;left:720px;width:340px;font-size:12.5px;line-height:27px;color:var(--body)}

/* services */
.services{top:1670px;height:800px;background:var(--soft)}
.section-title{font-size:40px;font-weight:500;text-align:center;position:absolute;width:1200px;top:105px}
.svc-box{position:absolute;left:135px;top:191px;width:928px;height:503px;background:var(--white)}
.svc-frame{position:absolute;left:156px;top:220px;width:887px;height:446px;border:2px solid var(--line)}
.card{position:absolute;top:259px;width:262px;height:369px;background:#f6f6f6}
.card .img{height:164px}
.card .badge{position:absolute;left:0;top:0;width:56px;height:56px;background:var(--brand);display:flex;align-items:center;justify-content:center}
.card h3{position:absolute;left:26px;top:196px;font-size:17px;font-weight:600}
.card p{position:absolute;left:26px;top:233px;width:215px;font-size:10.5px;line-height:20px;color:var(--body)}
.card .more{position:absolute;left:26px;top:329px;font-size:12px;font-weight:600;color:var(--navy);display:flex;align-items:center;gap:14px}
.arrow-btn{position:absolute;top:432px;width:48px;height:48px;border-radius:50%;background:var(--hero);display:flex;align-items:center;justify-content:center}

/* testimonials */
.testimonials{top:2470px;height:695px}
.testimonials h2{position:absolute;left:135px;top:130px;font-size:40px;font-weight:500;line-height:48px}
.t-intro{position:absolute;left:668px;top:140px;width:400px;font-size:12.5px;line-height:27px;color:var(--body)}
.t-card{position:absolute;top:277px;width:451px;height:304px}
.t-card p{position:absolute;left:38px;top:40px;width:385px;font-size:12.5px;line-height:25.5px;color:var(--body)}
.avatar{position:absolute;left:38px;top:207px;width:52px;height:52px;border-radius:50%;background:linear-gradient(135deg,#d9d3cc,#8f8276)}
.t-name{position:absolute;left:110px;top:205px;font-size:14px;font-weight:600}
.t-role{position:absolute;left:110px;top:229px;font-size:11px;color:var(--muted)}
.quote{position:absolute;left:376px;top:212px}

/* contact */
.contact{top:3165px;height:901px;background:linear-gradient(180deg,#f1f1f1,#e9e9e9)}
.contact-photo{position:absolute;left:135px;top:115px;width:520px;height:671px;background:linear-gradient(160deg,#e8e4df,#d8c6bb 55%,#c4a9a0)}
.form-card{position:absolute;left:599px;top:174px;width:464px;height:551px;background:var(--white)}
.form-card h2{position:absolute;left:63px;top:62px;font-size:40px;font-weight:500}
.field{position:absolute;background:var(--soft);font-size:10px;color:var(--body);padding:16px 20px}

/* footer */
.site-footer{top:4066px;height:708px;background:var(--footer);color:var(--white)}
.f-logo{position:absolute;left:0;width:1200px;top:138px;display:flex;justify-content:center;align-items:center;gap:16px}
.f-logo .logo-square{width:32px;height:32px;background:var(--white)}
.f-logo .logo-name{font-size:50px;color:var(--white);font-weight:500}
.f-head{position:absolute;top:335px;font-size:22px;font-weight:500}
.f-text{position:absolute;left:143px;top:382px;width:250px;font-size:12.5px;line-height:27px}
.f-social{position:absolute;top:566px;width:38px;height:38px;border-radius:50%;background:rgba(255,255,255,.22)}
.f-divider{position:absolute;top:364px;width:1px;height:170px;background:rgba(255,255,255,.5)}
.f-links{position:absolute;left:530px;top:382px;font-size:11.5px;line-height:25px;list-style:none}
.f-contact{position:absolute;left:803px;display:flex;gap:18px;align-items:center;font-size:12.5px;line-height:23px}
.f-icon{width:32px;height:32px;border-radius:50%;background:var(--white);display:flex;align-items:center;justify-content:center;flex:none}
.f-rule{position:absolute;left:135px;top:650px;width:928px;height:1px;background:rgba(255,255,255,.4)}
.copy{position:absolute;left:0;width:1200px;top:676px;text-align:center;font-size:11.5px}
</style>
</head>
<body>

<header class="topbar">
  <div class="item" style="left:135px"><span class="dot-icon"><i></i></span>Opening Hours : 08:00AM to 21:00PM</div>
  <div class="item" style="left:484px"><span class="dot-icon"><i></i></span>hello@clearpathledgers.com</div>
  <div class="item follow">Follow Us On: <span class="social-dot"></span><span class="social-dot"></span><span class="social-dot"></span><span class="social-dot"></span></div>
</header>

<header class="site-header">
  <div class="logo-box"><span class="logo-square"></span><span class="logo-name">Clearpath Ledgers</span></div>
  <span class="nav active" style="left:406px">Home</span>
  <span class="nav" style="left:467px">About Us</span>
  <span class="nav" style="left:545px">Services</span>
  <span class="nav" style="left:620px">Pricing</span>
  <span class="nav" style="left:684px">Testimonials</span>
  <span class="nav" style="left:777px">Blogs</span>
  <span class="nav" style="left:837px">FAQs</span>
  <a class="btn btn-blue" style="left:928px;top:22px;width:132px;height:37px">Contact Us</a>
</header>

<section class="hero">
  <div class="hero-photo" role="img" aria-label="Eye doctor examining a young girl's eye with an ophthalmoscope"></div>
  <div class="hero-panel"></div>
  <h1>Unleashing<br>ClearPath Ledgers.</h1>
  <p>Lorem Ipsum is simply dummy text of the printing and typesetting industry. Lorem Ipsum has been</p>
  <a class="btn btn-white" style="left:928px;top:459px;width:132px;height:37px">Read More</a>
  <span class="scroll-line" style="top:150px;height:134px"></span>
  <span class="mouse"></span>
  <span class="scroll-line" style="top:389px;height:134px"></span>
</section>

<div class="features abs">
  <div class="feature" style="left:60px"><h3><span>01.</span>Lorem Ipsum</h3><p>Lorem Ipsum is simply dummy text of the printing and typesetting industry.</p></div>
  <div class="feature" style="left:347px"><h3><span>02.</span>Lorem Ipsum</h3><p>Lorem Ipsum is simply dummy text of the printing and typesetting industry.</p></div>
  <div class="feature" style="left:635px"><h3><span>03.</span>Lorem Ipsum</h3><p>Lorem Ipsum is simply dummy text of the printing and typesetting industry.</p></div>
</div>

<section class="about">
  <span class="corner" style="left:135px;top:50px;width:84px;height:85px"></span>
  <span class="corner" style="left:568px;top:466px;width:85px;height:89px"></span>
  <div class="about-photo" role="img" aria-label="Optometrist fitting trial frames for a smiling young girl"></div>
  <h2>About Us</h2>
  <p style="top:166px">Lorem Ipsum is simply dummy text of the printing and typesetting industry. Lorem Ipsum has been the industry's standard dummy text ever since the 1500s, when an unknown printer took a galley of type and scrambled it to make a type specimen book.</p>
  <p style="top:327px">It has survived not only five centuries, but also the leap into electronic typesetting, remaining essentially unchanged</p>
  <a class="btn btn-navy" style="left:720px;top:443px;width:132px;height:35px">Learn More</a>
</section>

<section class="services">
  <h2 class="section-title">Our Services</h2>
  <div class="svc-box"></div>
  <div class="svc-frame"></div>
  <a class="arrow-btn" style="left:65px"><svg width="14" height="14" viewBox="0 0 14 14"><path d="M9 2 4 7l5 5" fill="none" stroke="#fff" stroke-width="2.5"/></svg></a>
  <a class="arrow-btn" style="left:1085px"><svg width="14" height="14" viewBox="0 0 14 14"><path d="M5 2l5 5-5 5" fill="none" stroke="#fff" stroke-width="2.5"/></svg></a>

  <article class="card" style="left:184px">
    <div class="img" role="img" aria-label="Eye care consultation in a clinic" style="background:linear-gradient(135deg,#e6e2dc,#b9b1a6)"></div>
    <span class="badge"><svg width="28" height="18" viewBox="0 0 28 18"><path d="M2 9c4-6 20-6 24 0-4 6-20 6-24 0z" fill="none" stroke="#fff" stroke-width="2"/><circle cx="14" cy="9" r="4" fill="#fff"/></svg></span>
    <h3>Eye Care</h3>
    <p>Lorem Ipsum is simply dummy text of the printing and typesetting industry. Lorem Ipsum has been the industry's</p>
    <span class="more">Read More <svg width="36" height="8" viewBox="0 0 36 8"><path d="M0 4h34M30 1l4 3-4 3" fill="none" stroke="#1a2bb5" stroke-width="1.2"/></svg></span>
  </article>
  <article class="card" style="left:469px">
    <div class="img" role="img" aria-label="Patient having a retina examination" style="background:linear-gradient(135deg,#eceae6,#c5bdb3)"></div>
    <span class="badge"><svg width="28" height="24" viewBox="0 0 28 24"><path d="M2 7V2h5M21 2h5v5M26 17v5h-5M7 22H2v-5M5 12c3-5 15-5 18 0-3 5-15 5-18 0z" fill="none" stroke="#fff" stroke-width="2"/><circle cx="14" cy="12" r="3" fill="#fff"/></svg></span>
    <h3>Retina Repair</h3>
    <p>Lorem Ipsum is simply dummy text of the printing and typesetting industry. Lorem Ipsum has been the industry's</p>
    <span class="more">Read More <svg width="36" height="8" viewBox="0 0 36 8"><path d="M0 4h34M30 1l4 3-4 3" fill="none" stroke="#1a2bb5" stroke-width="1.2"/></svg></span>
  </article>
  <article class="card" style="left:753px">
    <div class="img" role="img" aria-label="Woman wearing trial frames during a vision check" style="background:linear-gradient(135deg,#e3ecf3,#b7c6d2)"></div>
    <span class="badge"><svg width="28" height="22" viewBox="0 0 28 22"><path d="M2 13c4-6 20-6 24 0-4 6-20 6-24 0z" fill="none" stroke="#fff" stroke-width="2"/><circle cx="14" cy="13" r="3.5" fill="#fff"/><path d="M14 2v3M7 4l2 2M21 4l-2 2" stroke="#fff" stroke-width="2"/></svg></span>
    <h3>Vision Check</h3>
    <p>Lorem Ipsum is simply dummy text of the printing and typesetting industry. Lorem Ipsum has been the industry's</p>
    <span class="more">Read More <svg width="36" height="8" viewBox="0 0 36 8"><path d="M0 4h34M30 1l4 3-4 3" fill="none" stroke="#1a2bb5" stroke-width="1.2"/></svg></span>
  </article>
</section>

<section class="testimonials">
  <h2>What Our Client<br>Says</h2>
  <span class="abs" style="left:599px;top:114px;width:1px;height:119px;background:#999"></span>
  <p class="t-intro">Lorem Ipsum is simply dummy text of the printing and typesetting industry. Lorem Ipsum has been the industry's standard dummy text ever since the 1500s,</p>

  <article class="t-card" style="left:135px;background:#fff;box-shadow:0 6px 22px rgba(0,0,0,.09)">
    <p>Lorem Ipsum is simply dummy text of the printing and typesetting industry. Lorem Ipsum has been the industry's standard dummy text ever since the 1500s, when an unknown printer took a galley of type and scrambled it to make a type specimen book.</p>
    <span class="avatar" role="img" aria-label="Portrait of the reviewer"></span>
    <span class="t-name">Daniel Harlow</span><span class="t-role">Manager</span>
    <svg class="quote" width="40" height="28" viewBox="0 0 40 28"><path d="M0 0h16v14L8 28H2l6-12H0zM22 0h16v14l-8 14h-6l6-12h-8z" fill="#1a2bb5"/></svg>
  </article>
  <article class="t-card" style="left:612px;background:var(--soft)">
    <p>Lorem Ipsum is simply dummy text of the printing and typesetting industry. Lorem Ipsum has been the industry's standard dummy text ever since the 1500s, when an unknown printer took a galley of type and scrambled it to make a type specimen book.</p>
    <span class="avatar" role="img" aria-label="Portrait of the reviewer"></span>
    <span class="t-name">Daniel Harlow</span><span class="t-role">Manager</span>
    <svg class="quote" width="40" height="28" viewBox="0 0 40 28"><path d="M0 0h16v14L8 28H2l6-12H0zM22 0h16v14l-8 14h-6l6-12h-8z" fill="#1a2bb5"/></svg>
  </article>
</section>

<section class="contact">
  <div class="contact-photo" role="img" aria-label="Girl looking through optometry trial frames held by a doctor"></div>
  <div class="form-card">
    <h2>Contact Us</h2>
    <div class="field" style="left:61px;top:139px;width:164px;height:43px">Your Name</div>
    <div class="field" style="left:238px;top:139px;width:167px;height:43px">Enter Email</div>
    <div class="field" style="left:61px;top:197px;width:164px;height:42px">Subject</div>
    <div class="field" style="left:238px;top:197px;width:167px;height:42px">Phone</div>
    <div class="field" style="left:61px;top:252px;width:344px;height:156px">Message</div>
    <a class="btn btn-blue" style="left:61px;top:449px;width:132px;height:35px">Submit Now</a>
  </div>
</section>

<footer class="site-footer">
  <div class="f-logo"><span class="logo-square"></span><span class="logo-name">Clearpath Ledgers</span></div>

  <h4 class="f-head" style="left:143px">About Us</h4>
  <p class="f-text">Lorem Ipsum is simply dummy text of the printing and typesetting industry. Lorem Ipsum has been the industry's</p>
  <span class="f-social" style="left:142px"></span>
  <span class="f-social" style="left:189px"></span>
  <span class="f-social" style="left:235px"></span>
  <span class="f-social" style="left:282px"></span>

  <span class="f-divider" style="left:455px"></span>
  <h4 class="f-head" style="left:530px">Quick Links</h4>
  <ul class="f-links"><li>Home</li><li>About Us</li><li>Services</li><li>Pricing</li><li>Testimonials</li><li>Blogs</li><li>FAQs</li><li>Contact Us</li></ul>

  <span class="f-divider" style="left:729px"></span>
  <h4 class="f-head" style="left:803px">Contact Us</h4>
  <div class="f-contact" style="top:387px"><span class="f-icon"><svg width="14" height="14" viewBox="0 0 14 14"><path d="M3 1l2 3-1.5 1.5a8 8 0 0 0 5 5L10 9l3 2-1.5 2.5C6 13 1 8 .5 2.5z" fill="#13269f"/></svg></span>555-014-2270</div>
  <div class="f-contact" style="top:444px"><span class="f-icon"><svg width="14" height="10" viewBox="0 0 14 10"><rect width="14" height="10" rx="1" fill="#13269f"/><path d="M1 1l6 4 6-4" fill="none" stroke="#fff" stroke-width="1"/></svg></span>info@clearpathledgers.com</div>
  <div class="f-contact" style="top:492px"><span class="f-icon"><svg width="12" height="16" viewBox="0 0 12 16"><path d="M6 0a6 6 0 0 1 6 6c0 4-6 10-6 10S0 10 0 6a6 6 0 0 1 6-6z" fill="#13269f"/><circle cx="6" cy="6" r="2" fill="#fff"/></svg></span>18 Linden Row,<br>Marlow Bay 4021</div>

  <span class="f-rule"></span>
  <p class="copy">© Copyright 2023 <b>Clearpath Ledgers</b> . All Rights Reserved</p>
</footer>

</body>
</html>
```